KRV

I just wrote a novel that I plan on marketing through my website. Please use my uploaded files to add on to your design... The name of the book is "Ashes beneath the orchard".

Industry/Entity Type

Marketing

Font styles to use
Serif
Sans Serif

Colors

Designer to choose colors to be used in the design.

```html
<!DOCTYPE html>
<html lang="en">
<head>
<meta charset="utf-8">
<title>Ashes Beneath The Orchard — Marcus L. Thorne</title>
<link rel="stylesheet" href="https://fonts.googleapis.com/css2?family=Arimo:wght@400;700&family=Tinos:wght@400;700&family=Open+Sans:wght@400;600;700&display=swap">
<style>
:root{
  --ink:#222222;
  --grey:#6f6f6f;
  --grey-light:#8a8a8a;
  --rule:#9a9a9a;
  --frame:#dddddd;
  --crimson:#d4141c;
  --blood:#8a0a12;
  --navy:#231c60;
  --nav-active:#2a2a7a;
  --panel:#eeeeee;
  --white:#ffffff;
  --muted-white:#c9c6de;
}
*{margin:0;padding:0;box-sizing:border-box}
html,body{width:1200px;height:1000px;overflow:hidden;background:var(--white)}
body{position:relative;font-family:"Arimo",Arial,sans-serif;color:var(--grey)}
h1,h2,h3,h4,h5{font-weight:400}
.abs{position:absolute}
.drip{left:335px;top:0;width:105px;height:132px;background:linear-gradient(180deg,#9c0d17 0%,rgba(138,10,18,.55) 60%,rgba(138,10,18,0) 100%);border-radius:0 0 50% 50%}
.brand{left:0;width:1200px;top:26px;display:flex;justify-content:center;align-items:center;gap:8px}
.brand-dot{width:16px;height:16px;border-radius:50%;background:var(--ink)}
.brand-name{font-weight:700;font-size:30px;color:var(--ink);letter-spacing:2px}
.presents{left:0;width:1200px;top:84px;text-align:center;font-size:7px;color:var(--grey);letter-spacing:.3px}
.book-title{left:0;width:1200px;top:98px;text-align:center;font-family:"Tinos",serif;font-size:20px;color:var(--crimson);letter-spacing:.3px}
.author-line{left:423px;width:339px;top:131px;display:flex;align-items:center;gap:8px;font-size:11px;color:var(--grey);letter-spacing:.5px;white-space:nowrap}
.author-line::before,.author-line::after{content:"";flex:1;height:1px;background:var(--rule)}
.main-nav{left:0;width:1200px;top:157px;display:flex;justify-content:center;gap:16px;font-size:8.5px}
.main-nav a{color:var(--grey);text-decoration:none}
.main-nav a.active{color:var(--nav-active)}
.hero{left:334px;top:200px;width:539px;height:200px;
  background:linear-gradient(90deg,#ededed 0%,#e6e4e6 35%,#d9b7c8 60%,#b99acb 80%,#c9a17a 100%)}
.hero-book{left:428px;top:238px;width:140px;height:134px;background:linear-gradient(135deg,#8a3b52,#3a3f6e 60%,#c9c9d4)}
.hero-shadow{left:334px;top:398px;width:539px;height:12px;background:radial-gradient(ellipse at 50% 0%,rgba(0,0,0,.25),rgba(0,0,0,0) 70%)}
.hero-copy{left:598px;top:250px;width:265px}
.hero-copy h2{font-size:10px;font-weight:700;color:var(--ink);letter-spacing:.2px}
.hero-copy p{margin-top:20px;font-size:7.3px;line-height:9.6px;color:var(--white);text-shadow:0 0 2px rgba(0,0,0,.7)}
.hero-copy .more{display:block;margin-top:17px;font-size:6px;font-weight:700;color:var(--ink)}
.section-title{font-size:10px;font-weight:400;color:var(--grey);text-transform:uppercase;letter-spacing:.2px}
.body-copy{font-size:6.6px;line-height:9.2px;color:var(--grey-light)}
.welcome{left:334px;top:435px;width:322px}
.welcome .body-copy{margin-top:11px}
.about{left:334px;top:516px;width:322px}
.photo-frame{position:absolute;border:1px solid var(--frame);background:var(--white);padding:5px}
.about .photo-frame{left:0;top:20px;width:115px;height:80px}
.photo{width:100%;height:100%}
.author-photo{background:linear-gradient(90deg,#6f6560,#a58f80 45%,#efe3cf)}
.about .body-copy{position:absolute;left:124px;top:19px;width:195px}
.about .body-copy p+p{margin-top:9px}
.glance{left:703px;top:435px;width:170px}
.glance .photo-frame{left:0;top:23px;width:170px;height:96px;padding:5px 7px}
.cover-photo{background:linear-gradient(180deg,#8a6a5a,#d22a2a 40%,#c42020 60%,#6a5a52)}
.glance .body-copy{position:absolute;top:129px;width:170px}
.lower{left:0;top:637px;width:1200px;height:363px;background:var(--navy)}
.reviews .section-title,.blogs .section-title{color:var(--white)}
.reviews{left:334px;top:671px;width:250px}
.review-head{margin-top:17px;font-size:7.3px;font-weight:700;color:var(--white)}
.review-head span{color:var(--crimson)}
.reviews .body-copy{margin-top:14px;color:var(--white)}
.blogs{left:614px;top:671px;width:259px}
.blog-card{margin-top:17px;height:81px;background:var(--panel);padding:15px 16px}
.blog-card h3{font-size:7.5px;color:var(--grey)}
.blog-card p{margin-top:7px;font-size:6.4px;line-height:9px;color:var(--grey-light)}
.blog-card p span{color:#7aa21a}
.blog-meta{margin-top:10px;font-size:7px;font-weight:700;color:var(--white)}
.blog-meta em{font-weight:400;font-size:6px;color:var(--muted-white);margin-left:4px}
.divider{left:336px;top:830px;width:536px;border-top:1px dashed #5c5690}
.footer{font-family:"Open Sans",Arial,sans-serif}
.foot-brand{left:334px;top:858px;width:190px}
.foot-brand h4{font-family:"Tinos",serif;font-size:13px;color:var(--white)}
.foot-brand .by{font-size:7px;color:var(--crimson);letter-spacing:.3px}
.foot-brand .mail{margin-top:18px;font-size:6.5px;color:var(--white)}
.foot-brand .mail b{font-weight:600}
.foot-brand .copy{margin-top:10px;font-size:5.5px;color:var(--muted-white)}
.foot-col h5{font-size:7px;font-weight:700;color:var(--muted-white);letter-spacing:.2px}
.tweets{left:538px;top:862px;width:140px}
.tweet{margin-top:15px;font-size:6.5px;line-height:9.5px;color:var(--grey-light)}
.tweet b{color:var(--muted-white);font-weight:600}
.tweet small{display:block;font-size:5px;color:var(--muted-white);line-height:8px}
.tweet+.tweet{border-top:1px solid #4a4485;padding-top:9px;margin-top:6px}
.social{left:722px;top:862px;width:140px}
.social ul{list-style:none;margin-top:12px}
.social li{display:flex;align-items:center;gap:14px;height:19px;font-size:7px;font-weight:700;color:var(--muted-white)}
.social li i{width:5px;height:5px;border-radius:50%;background:var(--muted-white)}
</style>
</head>
<body>
<header class="site-header">
  <div class="abs drip" role="img" aria-label="Dripping red ink splash decoration"></div>
  <div class="abs brand"><span class="brand-dot"></span><span class="brand-name">KRV</span></div>
  <div class="abs presents">PRESENT'S</div>
  <h1 class="abs book-title">ASHES BENEATH THE ORCHARD</h1>
  <div class="abs author-line">AUTHOR : MARCUS L. THORNE</div>
  <nav class="abs main-nav">
    <a class="active" href="#">Home</a><a href="#">Reviews</a><a href="#">About Us</a><a href="#">Blogs</a><a href="#">Contact Us</a>
  </nav>
</header>

<section class="abs hero" role="img" aria-label="Soft blurred photo of coloured pencils behind the book"></section>
<div class="abs hero-book" role="img" aria-label="Novel cover shown as a standing book mock-up"></div>
<div class="abs hero-shadow"></div>
<div class="abs hero-copy">
  <h2>ASHES BENEATH THE ORCHARD</h2>
  <p>Lorem Ipsum is simply dummy text of the printing and typesetting industry. Lorem Ipsum has been the industry's standard dummy text ever since the 1500s, when an unknown printer took a galley of type and scrambled it to make a type specimen book.</p>
  <a class="more">CONTINUE...</a>
</div>

<section class="abs welcome">
  <h2 class="section-title">Welcome to our website !</h2>
  <p class="body-copy">Lorem Ipsum is simply dummy text of the printing and typesetting industry. Lorem Ipsum has been the industry's standard dummy text ever since the 1500s, when an unknown printer took a galley of type and scrambled it to make a type specimen book. It has survived not only five centuries, but also the leap into electronic typesetting, remaining essentially unchanged.</p>
</section>

<section class="abs about">
  <h2 class="section-title">About Author</h2>
  <div class="photo-frame"><div class="photo author-photo" role="img" aria-label="Portrait photo of the author"></div></div>
  <div class="body-copy">
    <p>Lorem Ipsum is simply dummy text of the printing and typesetting industry. Lorem Ipsum has been the industry's standard dummy text ever since the 1500s.</p>
    <p>when an unknown printer took a galley of type and scrambled it to make a type specimen book.</p>
  </div>
</section>

<section class="abs glance">
  <h2 class="section-title">At a glance..</h2>
  <div class="photo-frame"><div class="photo cover-photo" role="img" aria-label="Book cover artwork with title banner over a photo collage"></div></div>
  <p class="body-copy">Lorem Ipsum is simply dummy text of the printing and typesetting industry. Lorem Ipsum has been the industry's standard dummy text ever since the 1500s</p>
</section>

<div class="abs lower"></div>

<section class="abs reviews">
  <h2 class="section-title">Reviews of the book</h2>
  <p class="review-head">Unpolished, But Still a Gem &nbsp;By <span>Velden Studio</span></p>
  <p class="body-copy">Lorem Ipsum is simply dummy text of the printing and typesetting industry. Lorem Ipsum has been the industry's standard dummy text ever since the 1500s, when an unknown printer took a galley of type and &nbsp;and more recently with desktop publishing software like Folio PageSetter including versions of Lorem Ipsum. [.....]</p>
</section>

<section class="abs blogs">
  <h2 class="section-title">Blogs</h2>
  <article class="blog-card">
    <h3>- Harbour Party struggles for a clear purpose in the modern world</h3>
    <p>This week Prime Minister Alan Reeve announced the date of the next election. Predictably the Harbour Party led by Tom Ashcroft came out swinging <span>[.....]</span></p>
  </article>
  <p class="blog-meta">Author Marcus L. Thorne, <em>Friday, 26 May 2014</em></p>
</section>

<div class="abs divider"></div>

<footer class="footer">
  <div class="abs foot-brand">
    <h4>Ashes Beneath The Orchard</h4>
    <p class="by">AUTHOR : MARCUS L. THORNE</p>
    <p class="mail"><b>Email:</b> info@example.com</p>
    <p class="copy">Copyright 2014 &nbsp;All Right Reserved Company Name</p>
  </div>
  <div class="abs foot-col tweets">
    <h5>GET IN TWEET</h5>
    <p class="tweet"><b>@name</b> Lorem Ipsum is simply dummy text of the printing and typesetting industry<small>5 min ago</small></p>
    <p class="tweet"><b>@name</b> Lorem Ipsum is simply dummy text of the printing and typesetting industry<small>5 min ago</small></p>
  </div>
  <div class="abs foot-col social">
    <h5>GET IN TWEET</h5>
    <ul>
      <li><i></i>Connect Circlebook</li>
      <li><i></i>Get in Tweet</li>
      <li><i></i>Linkline</li>
    </ul>
  </div>
</footer>
</body>
</html>
```